Infographic for council approvals process

Looking to show the different steps that a person needs to undertake to get local council approval for their new swimming pool. It's a bit convoluted and text heavy when written out, but could be more graphically illustrated as a series of steps and choices.
Needs to be aligned to the brand for www.LagoonBuildPacksOnline.com.au

Target Market(s)

Home Owners

Font styles to use
Sans Serif

Requirements
Must have
• Nice graphics that help simplify and layout the process graphically, the infographic should reference our brand colours and logos.

```html
<!DOCTYPE html>
<html lang="en">
<head>
<meta charset="utf-8">
<title>Pool Approval – Approval Process for a Pool in NSW</title>
<link href="https://fonts.googleapis.com/css2?family=Jost:wght@400;500;600;700;800;900&display=swap" rel="stylesheet">
<style>
  :root{
    --stage:#000000;
    --paper:#ffffff;
    --navy:#173b62;
    --teal:#92d4d3;
    --teal-deep:#5fc2bf;
    --yellow:#f7cd3c;
    --blob:#d6eaf6;
    --ink:#1b1b1b;
    --muted:#4a4a4a;
    --shadow:rgba(0,0,0,.14);
  }
  *{box-sizing:border-box;margin:0;padding:0}
  html,body{width:1200px;height:1200px;overflow:hidden;background:var(--stage)}
  body{position:relative;font-family:"Jost",sans-serif;color:var(--ink)}
  .sheet{position:absolute;left:88px;top:200px;width:1024px;height:724px;background:var(--paper);overflow:hidden}
  .header-band{position:absolute;left:0;top:0;width:1024px;height:160px}
  .title{position:absolute;left:0;top:12px;width:100%;text-align:center;font-weight:900;font-size:38px;letter-spacing:1px;color:var(--navy)}
  .subtitle{position:absolute;left:0;top:60px;width:100%;text-align:center;font-size:12px;letter-spacing:.5px;color:var(--navy);font-weight:500}
  .state-pill{position:absolute;left:238px;top:84px;width:548px;height:31px;border-radius:16px;background:var(--yellow);text-align:center;line-height:31px;font-weight:800;font-size:19px;letter-spacing:.5px;color:var(--navy)}
  .step{position:absolute;top:186px;width:150px;margin-left:-75px;text-align:center}
  .step-blob{position:absolute;left:13px;top:-4px;width:124px;height:62px;border-radius:48% 52% 45% 55%/55% 45% 55% 45%;background:var(--blob)}
  .step-label{position:relative;font-size:16px;line-height:19px;color:var(--navy);font-weight:400;letter-spacing:.3px}
  .step-label b{font-weight:800}
  .step-icon{position:relative;display:block;margin:10px auto 0;width:42px;height:42px}
  .icon-slot{position:relative;margin:10px auto 0;width:40px;height:42px;border-radius:8px;background:linear-gradient(#c9dbe8,#9eb7cb)}
  .option{position:absolute;left:186px;width:160px;text-align:center}
  .option-num{font-weight:800;font-size:15px;color:var(--teal-deep)}
  .option-name{font-weight:800;font-size:15px;color:var(--navy);line-height:17px}
  .option-body{font-size:13px;color:var(--ink);line-height:16px}
  .badge{display:block;margin:6px auto 0}
  .doc-card{position:absolute;left:347px;width:160px;background:var(--paper);box-shadow:0 1px 5px var(--shadow);padding:7px 8px 7px 10px;font-size:10px;line-height:12px;color:var(--ink)}
  .doc-card ol{padding-left:13px}
  .doc-card .note{font-style:italic;margin-top:5px}
  .inspection{position:absolute;left:664px;top:326px;width:176px;text-align:center;font-size:12px;line-height:14px;color:var(--ink)}
  .inspection ul{list-style:none;margin-top:14px}
  .inspection li{font-weight:600}
  .inspection li::before{content:"";display:inline-block;width:5px;height:5px;border-radius:50%;background:var(--teal-deep);margin-right:5px;vertical-align:2px}
  .brand{position:absolute;left:692px;top:638px;display:flex;align-items:center;gap:12px}
  .brand-dot{width:34px;height:34px;border-radius:50%;background:var(--teal)}
  .brand-name{font-weight:800;font-size:21px;line-height:22px;color:var(--navy);letter-spacing:.3px}
  .credit{position:absolute;left:770px;top:700px;font-size:7px;color:var(--muted)}
</style>
</head>
<body>
<main class="sheet">
  <svg class="header-band" viewBox="0 0 1024 160" aria-hidden="true">
    <path fill="var(--teal)" d="M0 0H1024V136
      q-21.33 -14 -42.67 0 q-21.33 14 -42.67 0 q-21.33 -14 -42.67 0 q-21.33 14 -42.67 0
      q-21.33 -14 -42.67 0 q-21.33 14 -42.67 0 q-21.33 -14 -42.67 0 q-21.33 14 -42.67 0
      q-21.33 -14 -42.67 0 q-21.33 14 -42.67 0 q-21.33 -14 -42.67 0 q-21.33 14 -42.67 0
      q-21.33 -14 -42.67 0 q-21.33 14 -42.67 0 q-21.33 -14 -42.67 0 q-21.33 14 -42.67 0
      q-21.33 -14 -42.67 0 q-21.33 14 -42.67 0 q-21.33 -14 -42.67 0 q-21.33 14 -42.67 0
      q-21.33 -14 -42.67 0 q-21.33 14 -42.67 0 q-21.33 -14 -42.67 0 q-21.33 14 -42.67 0
      H0Z"/>
  </svg>
  <h1 class="title">POOL APPROVAL</h1>
  <p class="subtitle">EACH STATE HAS ITS OWN APPROVAL PROCESS, REQUIRED PERMITS, COMPLIANCE STANDARDS, AND INSPECTION PROCEDURES.</p>
  <div class="state-pill">APPROVAL PROCESS FOR A POOL IN NSW</div>

  <section class="step" style="left:98px">
    <div class="step-blob"></div>
    <p class="step-label">UNDERSTAND<br><b>REGULATION</b></p>
    <svg class="step-icon" viewBox="0 0 42 42" fill="none" stroke="var(--navy)" stroke-width="2" stroke-linecap="round">
      <path d="M21 9a9 9 0 0 0-5 16.5V30h10v-4.5A9 9 0 0 0 21 9z"/><path d="M17 34h8M18 38h6"/>
      <path d="M21 2v3M7 8l2 2M35 8l-2 2M3 19h3M39 19h-3"/>
    </svg>
  </section>
  <section class="step" style="left:262px">
    <div class="step-blob"></div>
    <p class="step-label">SEEK<br>PROFESSIONAL<br><b>GUIDANCE</b></p>
    <div class="icon-slot" role="img" aria-label="Icon of a building professional in a hard hat" style="margin-top:6px"></div>
  </section>
  <section class="step" style="left:426px">
    <div class="step-blob"></div>
    <p class="step-label">DOCUMENT<br><b>SUBMISSION</b></p>
    <svg class="step-icon" viewBox="0 0 42 42" fill="none" stroke="var(--navy)" stroke-width="2" stroke-linejoin="round">
      <path d="M8 3h19l7 7v28H8z"/><path d="M27 3v7h7"/><path d="M13 14h10M13 19h16M13 24h12M13 29h8"/>
      <circle cx="30" cy="32" r="6" fill="var(--paper)"/><path d="M27.5 32l2 2 3-4"/>
    </svg>
  </section>
  <section class="step" style="left:590px">
    <div class="step-blob"></div>
    <p class="step-label">POOL<br><b>INSTALLATION</b></p>
    <div class="icon-slot" role="img" aria-label="Icon of an excavator digging"></div>
  </section>
  <section class="step" style="left:752px">
    <div class="step-blob"></div>
    <p class="step-label">POOL<br><b>INSPECTION</b></p>
    <svg class="step-icon" viewBox="0 0 42 42" fill="none" stroke="var(--navy)" stroke-width="2.4" stroke-linecap="round">
      <circle cx="17" cy="17" r="11"/><path d="M25 25l12 12"/>
    </svg>
  </section>
  <section class="step" style="left:914px">
    <div class="step-blob"></div>
    <p class="step-label">POOL<br><b>APPROVAL</b></p>
    <svg class="step-icon" viewBox="0 0 42 42" fill="none" stroke="var(--navy)" stroke-width="2" stroke-linejoin="round">
      <path d="M4 18h34l-4 20H8z"/><path d="M7 24h28"/><path d="M16 4v20M26 4v20M16 10h10M16 16h10"/>
    </svg>
  </section>

  <div class="option" style="top:378px">
    <p class="option-num">Option 1</p>
    <p class="option-name">CDC APPROVAL</p>
    <p class="option-body">Private Certifier</p>
    <svg class="badge" width="104" height="24" aria-hidden="true"><rect width="104" height="24" rx="2" fill="var(--navy)"/></svg>
  </div>
  <div class="option" style="top:590px">
    <p class="option-num">Option 2</p>
    <p class="option-name">DA APPROVAL</p>
    <p class="option-body">Local Council</p>
    <svg class="badge" width="34" height="34" aria-hidden="true"><circle cx="17" cy="17" r="16" fill="#d7262e"/></svg>
  </div>

  <div class="doc-card" style="top:314px">
    <ol>
      <li>CDC Application form</li>
      <li>Section 10.7 Certificate for the Site Address.</li>
      <li>Deposited Plan/88b.</li>
      <li>Title Search</li>
      <li>Architectural Plans</li>
      <li>Local Water Authority Endorsement</li>
      <li>Pool Engineering Drawings</li>
      <li>BASIX Certificate (Building Sustainability Index) if your pool is over 40,000L capacity</li>
    </ol>
    <p class="note">Additional documents may be requested depending on your site</p>
  </div>
  <div class="doc-card" style="top:536px">
    <ol>
      <li>Statement of Environmental Effect (SEE)</li>
      <li>Site Survey/Plan</li>
      <li>Detailed DA Design Drawings.</li>
      <li>Structural Engineers Pool Drawings and Certification</li>
      <li>Builders Home Warranty Insurance</li>
      <li>Copy of payment receipt for Long Service Levy</li>
      <li>Water Authority Tap In Approval</li>
    </ol>
  </div>

  <div class="inspection">
    <p>An inspector<br>will visit the site<br>and ensure all<br>regulations have<br>been met:</p>
    <ul>
      <li>measurements</li>
      <li>tests</li>
      <li>photographs of<br>your pool gates,</li>
      <li>pool fences</li>
      <li>dividing fences<br>utilised as pool fences</li>
      <li>any objects or structures<br>in close proximity<br>to the pool fence.</li>
    </ul>
  </div>

  <div class="brand">
    <span class="brand-dot"></span>
    <span class="brand-name">LAGOON BUILD<br>PACKS ONLINE</span>
  </div>
  <p class="credit">Icons by Pictoform from Glyphnest</p>
</main>
</body>
</html>
```